Local Flower Farm Needs Business Card Design

I need business cards designed for a flower farm based in Eudora, Kansas.
Business Info:
We are a local cut flower farm located in Eudora, Kansas, founded by Darla Whitcombe. What started as a passion for agriculture and search for more joy in daily life has blossomed into a small business dedicated to providing the community with beautiful, fresh, and sustainable flowers. We specialize in local, seasonal blooms, ensuring that every petal reflects the care and dedication we pour into our craft. Our mission is to deliver the highest quality flowers directly to our customers through local farmers markets and to florists who share our commitment to sustainability. Join us in celebrating the beauty of nature, one bloom at a time!
Contact Details:
Darla Whitcombe
Owner
Phone 913-555-0148
Facebook: Rosalind Pike Gardens
Instagram: @RosalindPikeGardens
Website: RosalindPikeGardens.example
Target Market(s)
Wholesale to Florists and Direct to Consumer via Farmers Market
Industry/Entity Type
Florist, Farm
Contact Information for Business Card
Name, Contact Info, Logo
Look and feel
Each slider illustrates characteristics of the customer's brand and the style your logo design should communicate.

```html
<!DOCTYPE html>
<html lang="en">
<head>
<meta charset="utf-8">
<title>Rosalind Pike Gardens — Business Card</title>
<link rel="stylesheet" href="https://fonts.googleapis.com/css2?family=Arimo:wght@400;700&family=Cormorant+Garamond:wght@500&display=swap">
<style>
  :root {
    --backdrop: #2b2b2b;
    --teal: #0f2a2e;
    --paper: #ffffff;
    --ink-soft: #5a5f60;
    --logo-serif: "Cormorant Garamond", serif;
    --body-sans: "Arimo", sans-serif;
  }
  * { box-sizing: border-box; margin: 0; padding: 0; }
  html, body { width: 1200px; height: 900px; overflow: hidden; }
  body {
    background: var(--backdrop);
    display: flex;
    flex-direction: column;
    align-items: center;
    justify-content: center;
    gap: 36px;
    font-family: var(--body-sans);
  }
  .card {
    width: 700px;
    height: 400px;
    border-radius: 26px;
    position: relative;
    box-shadow: 0 10px 28px rgba(0,0,0,0.45);
  }
  .card--back { background: var(--teal); display: flex; align-items: center; justify-content: center; }
  .card--front { background: var(--paper); color: var(--teal); }

  .brand-seal {
    border-radius: 50%;
    display: flex;
    align-items: center;
    justify-content: center;
    text-align: center;
    font-family: var(--logo-serif);
    font-weight: 500;
    letter-spacing: 0.08em;
    text-transform: uppercase;
    line-height: 1.25;
  }
  .card--back .brand-seal {
    width: 200px; height: 200px;
    border: 1.5px solid var(--paper);
    color: var(--paper);
    font-size: 22px;
  }
  .card--front .brand-seal {
    position: absolute;
    top: 28px; right: 48px;
    width: 180px; height: 180px;
    border: 1.5px solid var(--teal);
    color: var(--teal);
    font-size: 20px;
  }

  .contact-block { position: absolute; left: 60px; bottom: 42px; }
  .contact-name { font-size: 27px; font-weight: 700; letter-spacing: 0.02em; text-transform: uppercase; }
  .contact-role { font-size: 17px; color: var(--ink-soft); margin-top: 2px; }
  .contact-rule { width: 12px; height: 1.5px; background: var(--ink-soft); margin: 16px 0 12px; }
  .contact-list { list-style: none; }
  .contact-list li {
    display: flex; align-items: center; gap: 8px;
    font-size: 18px; color: var(--ink-soft); line-height: 1.5;
  }
  .contact-icon { width: 14px; height: 14px; flex: none; }
</style>
</head>
<body>
  <section class="card card--back" aria-label="Card back">
    <div class="brand-seal">Rosalind<br>Pike<br>Gardens</div>
  </section>

  <section class="card card--front" aria-label="Card front">
    <div class="brand-seal">Rosalind<br>Pike<br>Gardens</div>
    <div class="contact-block">
      <h1 class="contact-name">Darla Whitcombe</h1>
      <p class="contact-role">Owner</p>
      <div class="contact-rule"></div>
      <ul class="contact-list">
        <li>
          <svg class="contact-icon" viewBox="0 0 24 24" aria-hidden="true"><path fill="#0f2a2e" d="M6.6 10.8a15.1 15.1 0 0 0 6.6 6.6l2.2-2.2a1 1 0 0 1 1-.25 11.4 11.4 0 0 0 3.6.57 1 1 0 0 1 1 1V20a1 1 0 0 1-1 1A17 17 0 0 1 3 4a1 1 0 0 1 1-1h3.5a1 1 0 0 1 1 1c0 1.25.2 2.45.57 3.6a1 1 0 0 1-.25 1z"/></svg>
          913-555-0148
        </li>
        <li>
          <svg class="contact-icon" viewBox="0 0 24 24" aria-hidden="true"><circle cx="12" cy="12" r="10" fill="#0f2a2e"/></svg>
          Rosalind Pike Gardens
        </li>
        <li>
          <svg class="contact-icon" viewBox="0 0 24 24" aria-hidden="true"><circle cx="12" cy="12" r="10" fill="#0f2a2e"/></svg>
          @RosalindPikeGardens
        </li>
        <li>
          <svg class="contact-icon" viewBox="0 0 24 24" aria-hidden="true"><circle cx="12" cy="12" r="9.5" fill="none" stroke="#0f2a2e" stroke-width="2"/><path d="M2.5 12h19M12 2.5c3 3 3 16 0 19M12 2.5c-3 3-3 16 0 19" fill="none" stroke="#0f2a2e" stroke-width="1.6"/></svg>
          RosalindPikeGardens.example
        </li>
      </ul>
    </div>
  </section>
</body>
</html>
```